Redesign of Business Card to look more professional and stand out

Business card design. You can lean more about our company by going to dlmfabworks.example. Raised letters would be nice. Company name & Address
DL&M
418 Wrenfield Crest Drive, Suite 140
Birmingham, AL 35999

You can use my name and title: Glenn Marlowe
Business Development Manager

Target Market(s)

Heavy Industrial market, i.e. utilities, chemical plants, paper mills, construction companies

Industry/Entity Type

Construction

Contact Information for Business Card

We provide Project Management & Project Support Services

Font styles to use
Serif

Requirements
Must have
• Company name & Address
• DL&M
• 418 Wrenfield Crest Drive, Suite 140
• Birmingham, AL 35999
Nice to have
• ideas for the back of the card
Should not have
• no crazy colors. needs to look professional and standout.

```html
<!DOCTYPE html>
<html lang="en">
<head>
<meta charset="utf-8">
<title>DL&amp;M Business Card</title>
<link rel="stylesheet" href="https://fonts.googleapis.com/css2?family=Noto+Serif:wght@400;700&display=swap">
<style>
  :root {
    --navy: #1b3a6b;
    --navy-deep: #163160;
    --steel: #2f64a0;
    --paper: #ffffff;
    --stage: #2a2a2c;
    --grey-name: #9a9ca3;
    --line: #7f86b5;
  }
  * { margin: 0; padding: 0; box-sizing: border-box; }
  html, body { width: 1200px; height: 900px; overflow: hidden; }
  body {
    background: var(--stage);
    position: relative;
    font-family: "Noto Serif", Georgia, serif;
  }
  .card {
    position: absolute;
    width: 620px;
    height: 354px;
    border-radius: 18px;
    overflow: hidden;
    background: var(--paper);
  }
  .card svg.shapes { position: absolute; inset: 0; width: 100%; height: 100%; }

  /* Back */
  .card-back { left: 90px; top: 70px; }
  .back-wordmark {
    position: absolute;
    left: 210px;
    top: 66px;
    font-weight: 700;
    font-size: 108px;
    letter-spacing: 2px;
    color: var(--steel);
    line-height: 1;
  }

  /* Front */
  .card-front { left: 490px; top: 476px; }
  .front-wordmark {
    position: absolute;
    left: 30px;
    top: 112px;
    font-weight: 700;
    font-size: 76px;
    color: var(--navy);
    line-height: 1;
  }
  .person {
    position: absolute;
    right: 46px;
    top: 20px;
    text-align: right;
  }
  .person-name {
    font-size: 21px;
    letter-spacing: 1.5px;
    text-transform: uppercase;
    color: var(--grey-name);
    line-height: 1.1;
  }
  .person-title {
    font-size: 13px;
    font-weight: 700;
    color: var(--navy);
    letter-spacing: .3px;
  }
  .contact {
    position: absolute;
    left: 30px;
    top: 256px;
    font-size: 14px;
    color: var(--navy);
    line-height: 1.35;
  }
  .contact-row { display: flex; align-items: center; gap: 6px; }
  .contact-row svg { width: 12px; height: 12px; flex: none; }
</style>
</head>
<body>

  <section class="card card-back" aria-label="Card back">
    <svg class="shapes" viewBox="0 0 620 354" preserveAspectRatio="none" aria-hidden="true">
      <path d="M0 0 H620 V354 H380 C300 354 120 330 0 262 Z" fill="var(--navy)"/>
      <path d="M0 262 C120 330 300 354 380 354" fill="none" stroke="var(--line)" stroke-width="5"/>
    </svg>
    <div class="back-wordmark">DL&amp;M</div>
  </section>

  <section class="card card-front" aria-label="Card front">
    <svg class="shapes" viewBox="0 0 620 354" preserveAspectRatio="none" aria-hidden="true">
      <path d="M620 92 C604 220 524 310 400 354 H620 Z" fill="var(--navy)"/>
      <path d="M608 96 C592 220 512 310 386 354" fill="none" stroke="var(--line)" stroke-width="3"/>
      <circle cx="620" cy="22" r="14" fill="var(--navy-deep)"/>
      <line x1="250" y1="196" x2="566" y2="196" stroke="var(--navy)" stroke-width="1.5"/>
      <line x1="28" y1="246" x2="360" y2="246" stroke="var(--navy)" stroke-width="1.5"/>
    </svg>

    <div class="person">
      <div class="person-name">Glenn Marlowe</div>
      <div class="person-title">Business Development Manager</div>
    </div>

    <div class="front-wordmark">DL&amp;M</div>

    <div class="contact">
      <div>418 Wrenfield Crest Drive</div>
      <div>Suite 140 Birmingham, AL 35999</div>
      <div class="contact-row">
        <svg viewBox="0 0 24 24" aria-hidden="true"><path fill="var(--navy)" d="M6.6 10.8a15 15 0 0 0 6.6 6.6l2.2-2.2c.3-.3.7-.4 1-.2 1.1.4 2.3.6 3.6.6.6 0 1 .4 1 1V20c0 .6-.4 1-1 1A17 17 0 0 1 3 4c0-.6.4-1 1-1h3.5c.6 0 1 .4 1 1 0 1.3.2 2.5.6 3.6.1.3 0 .7-.2 1z"/></svg>
        <span>205.555.0148</span>
      </div>
      <div class="contact-row">
        <svg viewBox="0 0 24 24" aria-hidden="true"><rect x="2" y="5" width="20" height="14" rx="1.5" fill="none" stroke="var(--navy)" stroke-width="2"/><path d="M3 6l9 7 9-7" fill="none" stroke="var(--navy)" stroke-width="2"/></svg>
        <span>marlowegm@dlm-projectmgt.example</span>
      </div>
    </div>
  </section>

</body>
</html>
```